Voyage Wellness Point Business Cards

We need business cards for our new start-up online travel health clinic. Visit our website voyagewellpoint.ca for branding and more info.

Target Market(s)

Travellers

Industry/Entity Type

Business

Contact Information for Business Card

Mara Kowalczyk
mara@voyagewellpoint.ca
+1 555 283 0461
voyagewellpoint.ca

Font styles to use
Sans Serif

Colors
f68d4d

```html
<!DOCTYPE html>
<html lang="en">
<head>
<meta charset="utf-8">
<title>Voyage Wellness Point – Business Cards</title>
<link rel="stylesheet" href="https://fonts.googleapis.com/css2?family=Roboto:ital,wght@0,400;1,400&family=Roboto+Condensed:wght@700&display=swap">
<style>
  :root {
    --backdrop: #2b2b2b;
    --card-front: #f4f4f4;
    --card-back: #aaaaaa;
    --accent: #f68d4d;
    --ink: #3f3f3f;
    --muted: #8a8a8a;
    --art: #dedede;
    --white: #ffffff;
  }
  * { margin: 0; padding: 0; box-sizing: border-box; }
  html, body { width: 1200px; height: 960px; overflow: hidden; }
  body {
    background: var(--backdrop);
    font-family: "Roboto", Arial, sans-serif;
    position: relative;
  }
  .card {
    position: absolute;
    width: 600px;
    height: 343px;
  }
  .card--front { left: 314px; top: 113px; background: var(--card-front); }
  .card--back { left: 311px; top: 472px; background: var(--card-back); }

  .hero-art {
    position: absolute;
    left: 14px; top: 15px;
    width: 317px; height: 312px;
    border-radius: 40px;
    background: radial-gradient(ellipse at 50% 50%, var(--art) 0%, var(--card-front) 75%);
  }
  .holder-name {
    position: absolute;
    right: 37px; top: 56px;
    font-family: "Roboto Condensed", Arial, sans-serif;
    font-weight: 700;
    font-size: 23px;
    color: var(--accent);
    letter-spacing: 0.2px;
  }
  .name-tab {
    position: absolute;
    right: 0; top: 57px;
    width: 15px; height: 29px;
    background: var(--accent);
  }
  .contact-list {
    position: absolute;
    right: 38px; top: 176px;
    list-style: none;
    text-align: right;
    font-size: 14px;
    color: var(--ink);
    line-height: 19.5px;
  }
  .contact-list li { display: flex; justify-content: flex-end; align-items: center; gap: 5px; }
  .contact-list svg { width: 13px; height: 13px; fill: var(--accent); }

  .brand-front {
    position: absolute;
    right: 38px; top: 257px;
    text-align: right;
  }
  .brand-name {
    font-size: 23px;
    font-weight: 400;
    color: var(--accent);
    line-height: 1;
  }
  .brand-tagline {
    font-size: 10px;
    font-style: italic;
    color: var(--muted);
    margin-top: 3px;
  }

  .brand-back {
    position: absolute;
    left: 0; right: 0; top: 156px;
    text-align: center;
    color: var(--white);
  }
  .brand-back .brand-name { color: var(--white); font-size: 34px; }
  .brand-back .brand-tagline { color: var(--white); font-size: 13px; margin-top: 4px; padding-left: 110px; }
  .site-url {
    position: absolute;
    left: 0; right: 0; top: 290px;
    text-align: center;
    font-size: 13px;
    letter-spacing: 4px;
    color: var(--white);
  }
</style>
</head>
<body>
  <section class="card card--front">
    <div class="hero-art" role="img" aria-label="Large faint airplane silhouette decoration"></div>
    <h1 class="holder-name">MARA KOWALCZYK</h1>
    <div class="name-tab"></div>
    <ul class="contact-list">
      <li>+1 555 283 0461
        <svg viewBox="0 0 24 24" aria-hidden="true"><path d="M6.6 10.8a15.1 15.1 0 0 0 6.6 6.6l2.2-2.2c.3-.3.7-.4 1-.2 1.1.4 2.3.6 3.6.6.6 0 1 .4 1 1V20c0 .6-.4 1-1 1A17 17 0 0 1 3 4c0-.6.4-1 1-1h3.5c.6 0 1 .4 1 1 0 1.3.2 2.5.6 3.6.1.3 0 .7-.2 1z"/></svg>
      </li>
      <li>mara@voyagewellpoint.ca
        <svg viewBox="0 0 24 24" aria-hidden="true"><path d="M2 5h20v14H2zm2 2v.5l8 5 8-5V7l-8 5z"/></svg>
      </li>
      <li>www.voyagewellpoint.ca
        <svg viewBox="0 0 24 24" aria-hidden="true"><circle cx="12" cy="12" r="10"/><path d="M12 2v20M2 12h20" stroke="#f4f4f4" stroke-width="1.5" fill="none"/></svg>
      </li>
    </ul>
    <div class="brand-front">
      <p class="brand-name">Voyage Wellness Point</p>
      <p class="brand-tagline">Online Travel Health Experts</p>
    </div>
  </section>

  <section class="card card--back">
    <div class="brand-back">
      <p class="brand-name">Voyage Wellness Point</p>
      <p class="brand-tagline">Online Travel Health Experts</p>
    </div>
    <p class="site-url">www.voyagewellpoint.ca</p>
  </section>
</body>
</html>
```